Plakat-Design für Computer Hard- und Software Einzelhandel
Zielgruppe
Einzelhandel, Computer Hard- und Software
Zielgruppe jede Altersklasse
Zur Verwendung an Hauswand/Schaufensterüberklebung - sehr großes Format
Aufgabenstellung
- möglichst ausschließlich Vektorgrafik, alterntiv sehr sehr hochauflösende Grafiken
- Postergröße 4620x2070mm
- bereitgestelltes Logo soll großflächig unterkommen
- Gestaltung eines ansprechenden Hintergrundes
- möglichst Fotoshop-Formate (CS6) verwenden

```html
<!DOCTYPE html>
<html lang="de">
<head>
<meta charset="utf-8">
<title>Voltmarkt – Plakat</title>
<link rel="stylesheet" href="https://fonts.googleapis.com/css2?family=Archivo:ital,wght@1,900&display=swap">
<style>
  :root {
    --navy-deep: #1e2447;
    --navy: #233063;
    --blue-mid: #1f4fa8;
    --blue-glow: #3d8fe0;
    --cyan-glow: #6fd0ff;
    --globe-green: #2f9c7a;
    --white: #ffffff;
  }
  html, body {
    margin: 0;
    padding: 0;
    width: 1200px;
    height: 535px;
    overflow: hidden;
    background: var(--navy-deep);
  }
  .poster {
    position: relative;
    width: 1200px;
    height: 535px;
    overflow: hidden;
    background:
      radial-gradient(ellipse 430px 330px at 830px 265px, rgba(61,143,224,0.85) 0%, rgba(31,79,168,0.75) 45%, rgba(35,48,99,0) 100%),
      linear-gradient(90deg, var(--navy-deep) 0%, var(--navy-deep) 28%, var(--navy) 50%, var(--blue-mid) 75%, var(--navy) 100%);
    font-family: "Archivo", "Arial Black", sans-serif;
  }
  .headline {
    position: absolute;
    left: 46px;
    top: 36px;
    margin: 0;
    color: var(--white);
    font-weight: 900;
    font-style: italic;
    font-size: 56px;
    line-height: 75px;
    letter-spacing: 4px;
    text-transform: uppercase;
  }
  .headline span { display: block; }
  .globe-art {
    position: absolute;
    left: 615px;
    top: 55px;
    width: 420px;
    height: 420px;
    border-radius: 50%;
    background: radial-gradient(circle at 50% 50%,
      rgba(47,156,122,0.6) 0%,
      rgba(39,74,154,0.95) 40%,
      #2a56b0 58%,
      rgba(111,208,255,0.75) 68%,
      rgba(111,208,255,0.25) 80%,
      rgba(61,143,224,0) 100%);
  }
  .brand {
    position: absolute;
    right: 16px;
    bottom: 30px;
    display: flex;
    align-items: center;
    gap: 10px;
    color: var(--white);
    font-weight: 900;
    font-style: italic;
  }
  .brand-dot {
    width: 16px;
    height: 16px;
    background: var(--white);
  }
  .brand-name {
    font-size: 34px;
    line-height: 1;
    letter-spacing: 1px;
  }
</style>
</head>
<body>
  <main class="poster">
    <h1 class="headline">
      <span>Entdecken Sie</span>
      <span>das gesamte</span>
      <span>Elektronik</span>
      <span>Universum</span>
    </h1>
    <div class="globe-art" role="img" aria-label="Leuchtende digitale Weltkugel aus gepunkteten Kontinenten, umgeben von blauen und grünen Ringbändern"></div>
    <div class="brand">
      <div class="brand-dot"></div>
      <div class="brand-name">Voltmarkt</div>
    </div>
  </main>
</body>
</html>
```